I need a logo design and a business card design for a new strategy consultancy that I set up called Tessaron LLC. We help clients make strategically important decisions, cutting through the cloud of noise. The design should imply clarity, simplicity and wisdom.

```html
<!DOCTYPE html>
<html lang="en">
<head>
<meta charset="UTF-8">
<title>Tessaron LLC — Business Card</title>
<link href="https://fonts.googleapis.com/css2?family=Arimo:wght@400;700&family=Cinzel:wght@500&display=swap" rel="stylesheet">
<style>
  :root {
    --backdrop: #8a5a33;
    --card-light: #dcb889;
    --card-mid: #c9a06e;
    --card-dark: #b98f5f;
    --ink: #141008;
  }
  * { box-sizing: border-box; margin: 0; padding: 0; }
  html, body {
    width: 1200px;
    height: 900px;
    overflow: hidden;
    background: var(--backdrop);
  }
  .stage {
    position: relative;
    width: 1200px;
    height: 900px;
  }
  .card {
    position: absolute;
    left: 330px;
    width: 556px;
    height: 343px;
    background: linear-gradient(135deg, var(--card-light) 0%, var(--card-mid) 50%, var(--card-dark) 100%);
    color: var(--ink);
    font-family: "Arimo", Arial, sans-serif;
    text-align: center;
  }
  .card-front { top: 90px; }
  .card-back { top: 470px; }

  .person-name {
    position: absolute;
    top: 62px;
    width: 100%;
    font-family: "Cinzel", "Times New Roman", serif;
    font-weight: 500;
    font-size: 24px;
    letter-spacing: 0.5px;
  }
  .person-role {
    position: absolute;
    top: 88px;
    width: 100%;
    font-size: 16px;
  }
  .rule {
    position: absolute;
    left: 180px;
    width: 195px;
    height: 1px;
    background: var(--ink);
  }
  .rule-upper { top: 117px; }
  .rule-lower { top: 222px; }
  .contact-list {
    position: absolute;
    top: 129px;
    width: 100%;
    list-style: none;
    font-size: 16px;
    line-height: 20px;
  }
  .contact-list b { font-weight: 700; }
  .address {
    position: absolute;
    top: 240px;
    width: 100%;
    font-size: 16px;
    line-height: 19px;
    font-style: normal;
  }

  .company-name {
    position: absolute;
    top: 140px;
    width: 100%;
    font-size: 34px;
    font-weight: 400;
    letter-spacing: 1px;
  }
</style>
</head>
<body>
  <main class="stage">
    <section class="card card-front">
      <h1 class="person-name">DANIEL MARLOWE</h1>
      <p class="person-role">Managing Director</p>
      <div class="rule rule-upper"></div>
      <ul class="contact-list">
        <li><b>P:</b> 044-555 018 240</li>
        <li><b>M:</b> 044-555 018 240</li>
        <li><b>E:</b> info@tessaron-mail.com</li>
        <li><b>W:</b> www.tessaron-site.com</li>
      </ul>
      <div class="rule rule-lower"></div>
      <address class="address">4820, Meridian Street<br>Westland, 204817.</address>
    </section>

    <section class="card card-back">
      <p class="company-name">Tessaron LLC</p>
    </section>
  </main>
</body>
</html>
```